Brom Vela CEO and Partners Business Card

We need a fresh, fun, simple and clean business card design....we would like a template where we can add a name and title (as well as specific email addresses). We are open to different looks (full logo on one side and a small logo on the company info side, or our logo is in the background but faint on one side but full on the other, or something else cool :-) ). Our colors are in our logo: blue, black and white...however we are not opposed to the use of other colors if it works. We build sets, make props and a host of other things for the film and television industry...our card should reflect creativity, style and professionalism.

A white background would be preferred.

I would like to see an option with Facebook and Instagram icons.

Facebook- facebook.com/bromvelaqt
Instagram- brom_vela

Our website is bromvela-example.com.

Brom Vela, Inc.
4168 Tolliver Crescent, Unit 9
Marden Falls, Oregon 97421
555.210.4872 | tel
555.210.6391 | fax
www.BromVela-example.com

Sample Name and Title #1:

Curtis Welbore
CEO / Co-Owner
555.210.4872 | tel
555.210.6391 | fax
curtis@bromvela-example.com
www.BromVela-example.com

Target Market(s)

Marketing Professionals, Production Designers, Interior Designers, Film Producers, Directors, Art Directors, Event Directors

Industry/Entity Type

Entertainment Industry

Contact Information for Business Card

Curtis Welbore
CEO / Co-Owner
555.210.4872 | tel
555.210.6391 | fax
curtis@bromvela-example.com
www.BromVela-example.com

Font styles to use
Sans Serif

Colors
33a6d7
ffffff
1b1b1b

Requirements
Must have
• Logo, All Contact Info, White Background. Symmetry.
Nice to have
• Facebook and Instagram icons with addresses
• Facebook- facebook.com/bromvelaqt
• Instagram- brom_vela

```html
<!DOCTYPE html>
<html lang="en">
<head>
<meta charset="utf-8">
<title>Brom Vela CEO and Partners Business Card</title>
<link rel="stylesheet" href="https://fonts.googleapis.com/css2?family=Open+Sans:wght@300;400;800&display=swap">
<style>
  :root {
    --brand-blue: #33a6d7;
    --brand-black: #1b1b1b;
    --card-white: #ffffff;
    --backdrop: #e9e9e9;
  }
  * { margin: 0; padding: 0; box-sizing: border-box; }
  html, body {
    width: 1200px;
    height: 1200px;
    overflow: hidden;
    background: var(--backdrop);
    font-family: "Open Sans", Arial, sans-serif;
  }
  .canvas {
    width: 1200px;
    height: 1200px;
    display: flex;
    align-items: center;
    justify-content: center;
  }
  .business-card {
    position: relative;
    width: 1000px;
    height: 572px;
    background: var(--card-white);
    box-shadow: 0 4px 18px rgba(0,0,0,0.12);
  }
  .brand-name {
    position: absolute;
    left: 170px;
    top: 150px;
    display: flex;
    align-items: center;
    gap: 18px;
    font-weight: 800;
    font-size: 84px;
    letter-spacing: -1px;
    color: var(--brand-black);
    line-height: 1;
  }
  .brand-mark {
    width: 34px;
    height: 34px;
    background: var(--brand-blue);
  }
  .identity {
    position: absolute;
    right: 590px;
    top: 392px;
    text-align: right;
  }
  .person-name {
    font-weight: 300;
    font-size: 38px;
    color: var(--brand-black);
    letter-spacing: -0.5px;
    white-space: nowrap;
  }
  .person-title {
    font-weight: 400;
    font-size: 20px;
    color: var(--brand-blue);
    margin-top: 2px;
  }
  .divider {
    position: absolute;
    left: 430px;
    top: 318px;
    width: 3px;
    height: 172px;
    background: var(--brand-black);
  }
  .contact-list {
    position: absolute;
    left: 458px;
    top: 318px;
    list-style: none;
  }
  .contact-item {
    display: flex;
    align-items: flex-start;
    gap: 12px;
    font-size: 19px;
    line-height: 27px;
    color: var(--brand-black);
    font-weight: 400;
  }
  .contact-icon {
    flex: 0 0 20px;
    width: 20px;
    height: 20px;
    margin-top: 4px;
  }
  .contact-icon rect { fill: var(--brand-blue); }
  .contact-icon .glyph { fill: none; stroke: var(--card-white); stroke-width: 1.6; }
  .contact-icon .glyph-fill { fill: var(--card-white); }
</style>
</head>
<body>
<main class="canvas">
  <section class="business-card">
    <div class="brand-name"><span>BROM VELA</span><span class="brand-mark"></span></div>

    <div class="identity">
      <p class="person-name">Curtis Welbore</p>
      <p class="person-title">CEO / Co-Owner</p>
    </div>

    <div class="divider"></div>

    <ul class="contact-list">
      <li class="contact-item">
        <svg class="contact-icon" viewBox="0 0 20 20" aria-hidden="true">
          <rect width="20" height="20" rx="2"/>
          <path class="glyph-fill" d="M5 6c0-1 1-2 2-2h6c1 0 2 1 2 2v1h-3V6H8v1H5zM6 9h8l1 6H5z"/>
        </svg>
        <span>555.210.4872</span>
      </li>
      <li class="contact-item">
        <svg class="contact-icon" viewBox="0 0 20 20" aria-hidden="true">
          <rect width="20" height="20" rx="2"/>
          <rect class="glyph" x="5" y="4" width="10" height="5" style="fill:none"/>
          <path class="glyph-fill" d="M4 10h12v6H4z"/>
        </svg>
        <span>555.210.6391</span>
      </li>
      <li class="contact-item">
        <svg class="contact-icon" viewBox="0 0 20 20" aria-hidden="true">
          <rect width="20" height="20" rx="2"/>
          <circle class="glyph" cx="10" cy="10" r="6"/>
          <path class="glyph" d="M4 10h12M10 4c-3 3-3 9 0 12M10 4c3 3 3 9 0 12"/>
        </svg>
        <span>www.BromVela-example.com</span>
      </li>
      <li class="contact-item">
        <svg class="contact-icon" viewBox="0 0 20 20" aria-hidden="true">
          <rect width="20" height="20" rx="2"/>
          <rect class="glyph" x="4" y="6" width="12" height="8"/>
          <path class="glyph" d="M4 6l6 5 6-5"/>
        </svg>
        <span>curtis@bromvela-example.com</span>
      </li>
      <li class="contact-item">
        <svg class="contact-icon" viewBox="0 0 20 20" aria-hidden="true">
          <rect width="20" height="20" rx="2"/>
          <path class="glyph-fill" d="M10 3a5 5 0 0 1 5 5c0 4-5 9-5 9s-5-5-5-9a5 5 0 0 1 5-5z"/>
          <circle cx="10" cy="8" r="2" fill="#33a6d7"/>
        </svg>
        <span>4168 Tolliver Crescent, Unit 9 Marden Falls,<br>Oregon 97421</span>
      </li>
    </ul>
  </section>
</main>
</body>
</html>
```